Design Menu card and product signage within shop for Indian fast food outlet

we are Indian Cafe style shop based in Sydney called Spice Lantern Lane Eats.
we sell Indian street food,tea,sweets and other fast food from the outlet

we will provide you pictures of few products with prices and size of banners/which will be displayed within shop inside to enhance and grab customer attraction

Target Market(s)

Indians and other communites all age group

Requirements
Must have
• pictures of Samosas, Panipuri,chaat , dosa,momos sweets can be included in menu
Nice to have
• Earthtone color schemes will be preferred and not too dark colors

```html
<!DOCTYPE html>
<html lang="en">
<head>
<meta charset="utf-8">
<title>Spice Lantern Lane Eats – Hot Snacks Menu</title>
<link rel="stylesheet" href="https://fonts.googleapis.com/css2?family=Lobster&family=Alegreya+Sans:ital,wght@0,400;1,300;1,400&display=swap">
<style>
  :root{
    --canvas:#ffffff;
    --frame:#9a9a9a;
    --cream:#f3e9d6;
    --cream-deep:#eadcc2;
    --bark:#4b3631;
    --bark-deep:#3f2d29;
    --ink:#3b2b26;
    --ink-soft:#4e3f39;
    --title:#5a3a30;
    --tag:#e6c52a;
    --tag-fold:#8c7414;
    --tag-ink:#4a3a1c;
    --logo:#ffffff;
    --caption:#7a7a7a;
    --no-mark:#c0392b;
  }
  *{box-sizing:border-box;margin:0;padding:0}
  html,body{width:1200px;height:975px;overflow:hidden;background:var(--canvas)}
  body{position:relative;font-family:"Alegreya Sans",sans-serif;color:var(--ink)}

  .spread{position:absolute;left:30px;top:40px;width:1142px;height:857px;border:1px solid var(--frame);overflow:hidden}
  .page{position:absolute;top:0;height:100%}
  .page--left{left:0;width:570px}
  .page--right{left:570px;width:572px}
  .paper{position:absolute;left:0;top:0;width:315px;height:100%;
    background:linear-gradient(160deg,var(--cream) 0%,#f6eedf 45%,var(--cream-deep) 100%)}
  .bark{position:absolute;left:315px;top:0;right:0;height:100%;
    background:radial-gradient(circle at 50% 40%,var(--bark) 0%,var(--bark-deep) 100%)}

  .brand{position:absolute;left:315px;right:0;top:70px;text-align:center;
    color:var(--logo);font-size:18px;font-weight:400;line-height:1.1}
  .brand::before{content:"";display:block;width:10px;height:10px;margin:0 auto 8px;background:var(--logo)}

  .section-title{position:absolute;left:47px;top:98px;font-family:"Lobster",cursive;
    font-size:36px;color:var(--title);font-weight:400}

  .item{position:absolute;left:47px;width:270px}
  .page--right .item{width:300px}
  .item__name{font-style:italic;font-weight:400;font-size:17px;line-height:20px;color:var(--ink)}
  .item__desc{font-style:italic;font-weight:300;font-size:9px;line-height:11.5px;color:var(--ink-soft)}
  .no-mark{display:inline-block;vertical-align:middle;margin-left:3px}

  .price{position:absolute;width:119px;height:26px;background:var(--tag);
    clip-path:polygon(0 0,100% 0,96% 100%,0 100%);
    font-style:italic;font-size:17px;color:var(--tag-ink);line-height:26px;padding-left:26px}
  .price small{font-size:10px}
  .price-fold{position:absolute;width:12px;height:12px;background:var(--tag-fold);
    clip-path:polygon(0 0,100% 0,100% 100%)}

  .photo{position:absolute;width:122px;height:130px;border:1px solid #ddd}
  .photo--samosa{background:radial-gradient(circle at 50% 55%,#e4b470 0%,#c98f45 30%,#f4f1ea 48%,#6b6460 75%)}
  .photo--vada{background:radial-gradient(circle at 45% 50%,#9a4a2a 0%,#b8643a 25%,#f3f0ea 48%,#5e5955 78%)}
  .photo--roll{background:linear-gradient(135deg,#3d6a2a 0%,#c78a3d 30%,#d9a15a 60%,#f2efe8 100%)}
  .photo--pav{background:radial-gradient(circle at 45% 60%,#e1b77a 0%,#f2efe8 45%,#6a6460 80%)}

  .caption{position:absolute;top:920px;font-size:27px;color:var(--caption);font-weight:400}
</style>
</head>
<body>
<div class="spread">

  <section class="page page--left">
    <div class="paper"></div>
    <div class="bark"></div>
    <div class="brand">Spice Lantern Lane Eats</div>
    <h1 class="section-title">Hot Snacks</h1>

    <div class="item" style="top:164px"><p class="item__name">Samosa</p><p class="item__desc">Fried pastry with a savoury filling made from spiced<br>potatoes and peas.<br>-No onions and garlic added<svg class="no-mark" width="26" height="12" viewBox="0 0 26 12"><circle cx="7" cy="6" r="4.5" fill="none" stroke="#6b5a50" stroke-width="1"/><circle cx="16" cy="6" r="4.5" fill="none" stroke="#6b5a50" stroke-width="1"/><line x1="1" y1="1" x2="25" y2="11" stroke="var(--no-mark)" stroke-width="1.3"/></svg></p></div>
    <div class="item" style="top:228px"><p class="item__name">Kachori</p><p class="item__desc">Fried pastry with a savoury filling made from lentils.<br>-No onions and garlic added<svg class="no-mark" width="26" height="12" viewBox="0 0 26 12"><circle cx="7" cy="6" r="4.5" fill="none" stroke="#6b5a50" stroke-width="1"/><circle cx="16" cy="6" r="4.5" fill="none" stroke="#6b5a50" stroke-width="1"/><line x1="1" y1="1" x2="25" y2="11" stroke="var(--no-mark)" stroke-width="1.3"/></svg></p></div>
    <div class="item" style="top:292px"><p class="item__name">Bread Pakora</p><p class="item__desc">Bread sandwiched with a savoury filling of potatoes and peas.<br>-No onions and garlic added<svg class="no-mark" width="26" height="12" viewBox="0 0 26 12"><circle cx="7" cy="6" r="4.5" fill="none" stroke="#6b5a50" stroke-width="1"/><circle cx="16" cy="6" r="4.5" fill="none" stroke="#6b5a50" stroke-width="1"/><line x1="1" y1="1" x2="25" y2="11" stroke="var(--no-mark)" stroke-width="1.3"/></svg></p></div>
    <div class="item" style="top:357px"><p class="item__name">Chilli Pakora</p><p class="item__desc">Long green chillies dipped in chickpea batter and fried.<br>-No onions and garlic added</p></div>
    <div class="item" style="top:421px"><p class="item__name">Onion Pakora</p><p class="item__desc">Onion sliced, dipped in chickpea batter<br>and fried to golden brown.</p></div>
    <div class="item" style="top:485px"><p class="item__name">Medhu Vada</p><p class="item__desc">South Indian fritter made from white urid lentil, usually made in<br>a doughnut shape, with a crispy exterior and soft interior.</p></div>
    <div class="item" style="top:550px"><p class="item__name">Masala Vada</p><p class="item__desc">Patties made by coarsely grinding soaked chana dal or<br>bengal gram (lentils) with spices, onions &amp; herbs.</p></div>
    <div class="item" style="top:614px"><p class="item__name">Aloo Bonda</p><p class="item__desc">Ball shaped fritters with a coating of chickpea batter filled<br>in with spiced potatoes.</p></div>
    <div class="item" style="top:678px"><p class="item__name">Mix Pakora</p><p class="item__desc">South Indian fritters of mixed vegetables such as cauliflower,<br>potatoes, capsicum, brinjal dipped in besan / chickpea flour<br>and fried till golden brown.</p></div>
    <div class="item" style="top:754px"><p class="item__name">Paneer Puff</p><p class="item__desc">Pastry Turnovers with a flaky golden crust with spicy<br>flavourful paneer (cottage cheese ) filling.</p></div>

    <div class="price" style="left:303px;top:162px">$2.50 <small>(each)</small></div><div class="price-fold" style="left:303px;top:188px"></div>
    <div class="price" style="left:303px;top:227px">$2.50 <small>(each)</small></div><div class="price-fold" style="left:303px;top:253px"></div>
    <div class="price" style="left:303px;top:291px">$2.50 <small>(each)</small></div><div class="price-fold" style="left:303px;top:317px"></div>
    <div class="price" style="left:303px;top:355px">$2.50 <small>(each)</small></div><div class="price-fold" style="left:303px;top:381px"></div>
    <div class="price" style="left:303px;top:419px">$2.50 <small>(each)</small></div><div class="price-fold" style="left:303px;top:445px"></div>
    <div class="price" style="left:303px;top:483px">$2.50 <small>(each)</small></div><div class="price-fold" style="left:303px;top:509px"></div>
    <div class="price" style="left:303px;top:548px">$2.50 <small>(each)</small></div><div class="price-fold" style="left:303px;top:574px"></div>
    <div class="price" style="left:303px;top:612px">$2.50 <small>(each)</small></div><div class="price-fold" style="left:303px;top:638px"></div>
    <div class="price" style="left:303px;top:677px">$2.50 <small>(each)</small></div><div class="price-fold" style="left:303px;top:703px"></div>
    <div class="price" style="left:303px;top:752px">$2.50 <small>(each)</small></div><div class="price-fold" style="left:303px;top:778px"></div>

    <div class="photo photo--samosa" style="left:448px;top:175px" role="img" aria-label="Photo of two samosas with chutneys on a white plate"></div>
    <div class="photo photo--vada" style="left:448px;top:344px" role="img" aria-label="Photo of masala vada fritters with dips on a white plate"></div>
    <div class="photo photo--roll" style="left:448px;top:513px" role="img" aria-label="Photo of crispy fried rolls with green chutney"></div>
    <div class="photo photo--pav" style="left:448px;top:683px" role="img" aria-label="Photo of pav buns with curry and salad on a plate"></div>
  </section>

  <section class="page page--right">
    <div class="paper"></div>
    <div class="bark"></div>
    <div class="brand">Spice Lantern Lane Eats</div>

    <div class="item" style="top:164px"><p class="item__name">Veg Puff</p><p class="item__desc">Pastry Turnovers with a flaky golden crust with<br>spicy flavourful vegetable filling.</p></div>
    <div class="item" style="top:224px"><p class="item__name">Veg Roll</p><p class="item__desc">Spring rolls filled with mix vegetables and coated with<br>breadcrumbs for crispy golden coloured fried snacks</p></div>
    <div class="item" style="top:284px"><p class="item__name">Chicken Roll</p><p class="item__desc">Spring rolls filled with minced chicken and spices,<br>coated with breadcrumbs for crispy golden coloured fried snacks</p></div>
    <div class="item" style="top:344px"><p class="item__name">Lamb Roll</p><p class="item__desc">Spring rolls filled with minced lamb, spices and coated with<br>breadcrumbs for crispy golden coloured fried snacks</p></div>
    <div class="item" style="top:404px"><p class="item__name">Vada Pav</p><p class="item__desc">Deep fried potato dumpling placed inside a bread bun/pav.<br>Perfect Mumbai side dish!</p></div>
    <div class="item" style="top:464px"><p class="item__name">Dabeli</p><p class="item__desc">It is a sweet &amp; savoury snack made by mixing boiled potatoes,<br>peanuts placed inside a bread bun/pav.</p></div>
    <div class="item" style="top:524px"><p class="item__name">Dahi Vada</p><p class="item__desc">South Indian fritter made from white urid lentil, usually made in a<br>&nbsp;doughnut shape, with a crispy exterior and soft interior soaked in<br>flavoured yogurt and given tadka for best taste.</p></div>

    <div class="price" style="left:305px;top:162px">$2.50 <small>(each)</small></div><div class="price-fold" style="left:305px;top:188px"></div>
    <div class="price" style="left:305px;top:222px">$2.50 <small>(each)</small></div><div class="price-fold" style="left:305px;top:248px"></div>
    <div class="price" style="left:305px;top:282px">$2.50 <small>(each)</small></div><div class="price-fold" style="left:305px;top:308px"></div>
    <div class="price" style="left:305px;top:342px">$2.50 <small>(each)</small></div><div class="price-fold" style="left:305px;top:368px"></div>
    <div class="price" style="left:305px;top:402px">$2.50 <small>(each)</small></div><div class="price-fold" style="left:305px;top:428px"></div>
    <div class="price" style="left:305px;top:462px">$2.50 <small>(each)</small></div><div class="price-fold" style="left:305px;top:488px"></div>
    <div class="price" style="left:305px;top:522px">$2.50 <small>(each)</small></div><div class="price-fold" style="left:305px;top:548px"></div>

    <div class="photo photo--samosa" style="left:448px;top:175px" role="img" aria-label="Photo of two samosas with chutneys on a white plate"></div>
    <div class="photo photo--vada" style="left:448px;top:344px" role="img" aria-label="Photo of masala vada fritters with dips on a white plate"></div>
    <div class="photo photo--roll" style="left:448px;top:513px" role="img" aria-label="Photo of crispy fried rolls with green chutney"></div>
  </section>
</div>

<p class="caption" style="left:231px">Menu inside Left Page 2</p>
<p class="caption" style="left:698px">Menu Right Page 3</p>
</body>
</html>
```